Tradeshow display - back drop and matching podium wrap

Looking for a design for a tradeshow display 136.22" x 90.55". and there is approximately 12.25" side panels on each side here (see attached). Needs design for matching podium wrap as well (specs attached).
You can take a look at our website to get a feel on who we are.
www.tillbrookflow.com
I've added a design I like so you get an idea of what I'm wanting here.
We do not want the Brookvane logos on the banner please.
We do water treatment using ozone.

Industry/Entity Type

Agriculture

Requirements
Should not have
• the brookvane logos

```html
<!DOCTYPE html>
<html lang="en">
<head>
<meta charset="utf-8">
<title>Tillbrook Flow – Tradeshow Backdrop and Podium Wrap</title>
<link rel="stylesheet" href="https://fonts.googleapis.com/css2?family=Oswald:wght@500;600;700&family=Roboto+Condensed:wght@700&display=swap">
<style>
  :root {
    --navy: #36456a;
    --navy-deep: #1f2a48;
    --ink: #243353;
    --grey-band: #e9eaec;
    --white: #ffffff;
    --page: #d6d6d6;
    --blue-dark: #1f5fae;
    --blue-mid: #2a7fc9;
    --leaf-light: #8cc63f;
    --leaf-dark: #0f6b35;
  }
  * { box-sizing: border-box; margin: 0; padding: 0; }
  html, body { width: 1200px; height: 840px; overflow: hidden; }
  body { background: var(--page); font-family: "Oswald", sans-serif; position: relative; }

  /* Podium wrap */
  .podium-wrap {
    position: absolute; left: 60px; top: 360px; width: 270px; height: 310px;
    background: linear-gradient(180deg, var(--navy) 0%, var(--navy-deep) 100%);
    display: flex; align-items: center; justify-content: center;
  }
  .podium-wrap .brand-name { font-size: 34px; gap: 10px; }
  .podium-wrap .brand-mark { width: 12px; height: 12px; }

  .brand-name {
    color: var(--white); font-weight: 700; letter-spacing: 0.5px; line-height: 1;
    display: flex; align-items: center; gap: 12px; white-space: nowrap;
  }
  .brand-mark { width: 16px; height: 16px; background: var(--white); flex: none; }

  /* Backdrop */
  .backdrop {
    position: absolute; left: 410px; top: 170px; width: 740px; height: 494px;
    background: var(--white); overflow: hidden;
  }
  .header-band {
    position: absolute; left: 0; top: 0; width: 100%; height: 150px;
    background: var(--navy);
    display: flex; align-items: center; justify-content: center;
  }
  .header-band .brand-name { font-size: 58px; }
  .tagline-band { position: absolute; left: 0; top: 150px; width: 100%; height: 105px; }
  .tagline-band svg { position: absolute; inset: 0; }

  .tagline {
    position: absolute; top: 21px; left: 50%; transform: translateX(-50%);
    display: flex; align-items: center; gap: 4px;
    color: var(--ink); font-weight: 600; font-size: 15px; white-space: nowrap;
  }
  .tagline-box {
    border: 1.5px solid var(--ink); border-radius: 6px; padding: 1px 9px; background: var(--white);
  }
  .tagline-equals {
    border: 1.5px solid var(--ink); border-radius: 3px; padding: 0 6px; font-size: 15px; line-height: 22px;
  }
  .url-pill {
    position: absolute; top: 56px; left: 50%; transform: translateX(-50%);
    background: var(--navy); color: var(--white); font-weight: 600; font-size: 16px;
    padding: 2px 22px; border-radius: 6px; letter-spacing: 0.3px; white-space: nowrap;
  }

  .side-url {
    position: absolute; top: 230px; height: 250px; width: 24px;
    writing-mode: vertical-rl; text-align: center;
    color: var(--ink); font-weight: 700; font-size: 12px; letter-spacing: 0.8px;
  }
  .side-url.left { left: 18px; }
  .side-url.right { right: 18px; transform: rotate(180deg); }

  .product-row {
    position: absolute; left: 70px; right: 70px; top: 270px;
    display: grid; grid-template-columns: repeat(4, 1fr); gap: 8px;
  }
  .product { text-align: center; color: var(--ink); }
  .product-icon { width: 66px; height: 80px; margin: 0 auto 14px; border-radius: 6px; }
  .icon-water { background: linear-gradient(160deg, var(--blue-mid), var(--blue-dark)); }
  .icon-plants { background: linear-gradient(150deg, var(--leaf-light), var(--leaf-dark)); border-radius: 50% 6px 50% 6px; }
  .product-title { font-weight: 600; font-size: 11.5px; letter-spacing: 0.2px; white-space: nowrap; }
  .product-copy {
    font-family: "Roboto Condensed", sans-serif; font-weight: 700; font-size: 8.5px;
    line-height: 1.3; margin: 7px auto 0; max-width: 122px;
  }
</style>
</head>
<body>

  <section class="podium-wrap" aria-label="Podium wrap">
    <div class="brand-name"><span class="brand-mark"></span>Tillbrook Flow</div>
  </section>

  <section class="backdrop" aria-label="Tradeshow backdrop">
    <header class="header-band">
      <div class="brand-name"><span class="brand-mark"></span>Tillbrook Flow</div>
    </header>

    <div class="tagline-band">
      <svg width="740" height="105" viewBox="0 0 740 105" preserveAspectRatio="none" aria-hidden="true">
        <polygon points="0,0 740,0 740,82 370,104 0,77" fill="var(--grey-band)"/>
      </svg>
      <div class="tagline">
        <span class="tagline-box">HIGH-QUALITY FARM WATER</span>
        <span class="tagline-equals">=</span>
        <span class="tagline-box">HEALTHY HIGH-PERFORMANCE FARMS</span>
      </div>
      <div class="url-pill">WWW.TILLBROOKFLOW.COM</div>
    </div>

    <div class="side-url left">WWW.TILLBROOKFLOW.COM</div>
    <div class="side-url right">WWW.TILLBROOKFLOW.COM</div>

    <div class="product-row">
      <article class="product">
        <div class="product-icon icon-water" role="img" aria-label="Dairy cow head with water drop icon"></div>
        <div class="product-title">DAIRY WATER TREATMENT</div>
        <p class="product-copy">Over the years our dairy systems have treated billions of gallons of water.</p>
      </article>
      <article class="product">
        <div class="product-icon icon-water" role="img" aria-label="Chicken head drinking water icon"></div>
        <div class="product-title">POULTRY WATER TREATMENT</div>
        <p class="product-copy">Take a look at our new Bio-Security system for poultry operations.</p>
      </article>
      <article class="product">
        <div class="product-icon icon-water" role="img" aria-label="Pig head drinking water icon"></div>
        <div class="product-title">SWINE WATER TREATMENT</div>
        <p class="product-copy">Quality water intake for swine operations is critical to both health and growth.</p>
      </article>
      <article class="product">
        <div class="product-icon icon-plants" role="img" aria-label="Two green leaves icon"></div>
        <div class="product-title">GREENHOUSE DISINFECTION</div>
        <p class="product-copy">Enhance both Greenhouse sanitation and plant performance.</p>
      </article>
    </div>
  </section>

</body>
</html>
```